【 概要 】 当社は、ペットフード商品を取り扱っております。 引き続き、犬用のおやつジャーキー商品ラベルデザインをお願いいたします。 作成物:犬のおやつで内容は、「鮭を使用した完全無添加、ヒューマングレードのジャーキー」です。 【 依頼詳細 】 ■詳細は、添付のエクセルデータに記載しております。 商品名:「北海道産 カリッと鶏ささみ棒(スライスタイプ)」です。 ■イメージ:エクセルデータにイメージを記載しています。 ※鮭の和と高級なイメージの中で親しみが出るようなソフトな雰囲気を意識していただきたいです。愛犬のおやつなので。 愛犬に安心安全で高級なおやつをあげたいと思いたくなるようなデザインを望んでいます。 ■ターゲット:愛犬に安心安全で高級なおやつをあげたいと思ってくれる飼い主様 【お願い】 採用となった方に修正などのご協力をお願いする場合がありますのでご了承ください。 ※デザインのイメージや柔軟なご対応にご協力いただけた場合、当社でも今後もデザインのご依頼を定期的にさせていただきたいと考えております。 ・編集可能なファイル形式(ai) ・PDFデータ ・フォトショップ(.psd) ・高解像度JPG形式(JPG) 【 契約金額(税込) 】 33,000円(税込) ※契約金額(税込)からシステム利用料を差し引いた金額が、ワーカーさまの受取金額となります ・採用されたデザインの著作権は弊社に譲渡いただき、同意いただいた上でご応募ください。 ■禁止事項 ------------------ ・他で登録されているデザインや転用など、他社の知的財産権を侵すこと ・他のクライアントへ既に提案した内容の転用など -------------------------------- 採用された方は継続的に仕事を依頼する場合もあります。 末永くお付き合いできるデザイナー様を探しております。 素敵なデザインに仕上げるために、ぜひお力をお貸しください その他ご質問等ありましたら、気軽にお問い合わせください。 ご応募をお待ちしております! |
こちらの作品が、当社としてもブランドのイメージに合ったデザインでした。ワーカー様もご対応が丁寧な方で好感をもてました。
皆様、素敵なデザインをご提案いただきありがとうございました。こんなにもご応募いただけたこと、うれしく存じます。また、機会があればご依頼させていただきますのでよろしくお願いいたします。

```html
<!DOCTYPE html>
<html lang="ja">
<head>
<meta charset="utf-8">
<title>カリッと鶏ささみ棒 パッケージ</title>
<link href="https://fonts.googleapis.com/css2?family=Yuji+Syuku&family=Noto+Sans+JP:wght@500;700&display=swap" rel="stylesheet">
<style>
  :root{
    --bg:#ffffff;
    --kraft:#c9a36e;
    --kraft-dark:#b38c58;
    --zip:#a7834f;
    --ink:#1c1c1c;
    --paper:#f1f0ec;
    --gold:#f2c21c;
    --sea-a:#5b86c4;
    --sea-b:#e8eef7;
    --grey-a:#7b7b7b;
    --grey-b:#eeeeee;
  }
  *{box-sizing:border-box;margin:0;padding:0}
  html,body{width:1200px;height:1200px;overflow:hidden;background:var(--bg)}
  .sheet{position:relative;width:1200px;height:1200px}
  .pouch{
    position:absolute;width:313px;height:522px;
    background:linear-gradient(90deg,var(--kraft-dark) 0,var(--kraft) 6%,var(--kraft) 94%,var(--kraft-dark) 100%);
    border-radius:4px;overflow:hidden;
  }
  .pouch--a{left:282px;top:39px}
  .pouch--b{left:738px;top:39px}
  .pouch--c{left:282px;top:626px}
  .pouch--d{left:738px;top:626px}
  .pouch__zip{position:absolute;left:0;right:0;top:40px;height:3px;background:var(--zip)}
  .pouch__hole{position:absolute;left:146px;top:14px;width:20px;height:8px;border-radius:4px;background:var(--bg)}
  .brand{
    position:absolute;left:14px;top:62px;width:34px;height:34px;background:var(--ink);
    color:#fff;font-family:"Noto Sans JP",sans-serif;font-weight:700;font-size:10px;
    display:flex;align-items:center;justify-content:center;
  }
  .label{
    position:absolute;left:50px;top:120px;width:220px;height:220px;border-radius:50%;
    background:var(--paper);
  }
  .pouch--c .label,.pouch--d .label{background:var(--ink)}
  .map{position:absolute;left:150px;top:112px;width:52px;height:44px;border-radius:40% 50% 35% 45%;background:var(--gold)}
  .pouch--b .map,.pouch--d .map{background:#d9d9d9}
  .name{position:absolute;z-index:2;font-family:"Yuji Syuku",serif;color:var(--ink);white-space:nowrap;line-height:1}
  .name__kanji{left:68px;top:180px;font-size:84px}
  .name__top{left:158px;top:208px;font-size:22px;letter-spacing:1px}
  .name__bottom{left:70px;top:274px;font-size:26px;letter-spacing:2px}
  .name__sub{left:76px;top:306px;font-family:"Noto Sans JP",sans-serif;font-size:8px;font-weight:500}
  .pouch--c .name,.pouch--d .name{color:#fff}
  .pouch--c .name__kanji{color:var(--gold)}
  .tate{
    position:absolute;z-index:2;writing-mode:vertical-rl;font-family:"Noto Sans JP",sans-serif;
    font-weight:500;font-size:8px;line-height:1;color:var(--ink);letter-spacing:1px;white-space:nowrap;
  }
  .tate--origin{left:272px;top:170px}
  .tate--claim-1{left:250px;top:262px}
  .tate--claim-2{left:237px;top:262px}
  .pouch--c .tate,.pouch--d .tate{color:#fff}
  .scene{
    position:absolute;z-index:1;left:22px;top:356px;width:270px;height:146px;
    border-radius:40% 40% 8px 8px / 30% 30% 8px 8px;
    background:linear-gradient(180deg,var(--sea-a),var(--sea-b));
  }
  .pouch--b .scene,.pouch--d .scene{background:linear-gradient(180deg,var(--grey-a),var(--grey-b))}
</style>
</head>
<body>
<main class="sheet">
  <section class="pouch pouch--a">
    <div class="pouch__hole"></div><div class="pouch__zip"></div>
    <div class="brand">ワン膳</div>
    <div class="label"></div>
    <div class="map" role="img" aria-label="北海道の地図イラスト"></div>
    <div class="name name__kanji">鶏</div>
    <div class="name name__top">カリッと</div>
    <div class="name name__bottom">ささみ棒</div>
    <div class="name name__sub">（スライスタイプ）</div>
    <div class="tate tate--origin">（北海道産おやつ）</div>
    <div class="tate tate--claim-1">完全無添加</div>
    <div class="tate tate--claim-2">ヒューマングレード</div>
    <div class="scene" role="img" aria-label="跳ねる魚と小舟に乗った犬、和柄の波のイラスト"></div>
  </section>
  <section class="pouch pouch--b">
    <div class="pouch__hole"></div><div class="pouch__zip"></div>
    <div class="brand">ワン膳</div>
    <div class="label"></div>
    <div class="map" role="img" aria-label="北海道の地図イラスト"></div>
    <div class="name name__kanji">鶏</div>
    <div class="name name__top">カリッと</div>
    <div class="name name__bottom">ささみ棒</div>
    <div class="name name__sub">（スライスタイプ）</div>
    <div class="tate tate--origin">（北海道産おやつ）</div>
    <div class="tate tate--claim-1">完全無添加</div>
    <div class="tate tate--claim-2">ヒューマングレード</div>
    <div class="scene" role="img" aria-label="モノクロの魚と犬、波のイラスト"></div>
  </section>
  <section class="pouch pouch--c">
    <div class="pouch__hole"></div><div class="pouch__zip"></div>
    <div class="brand">ワン膳</div>
    <div class="label"></div>
    <div class="map" role="img" aria-label="北海道の地図イラスト"></div>
    <div class="name name__kanji">鶏</div>
    <div class="name name__top">カリッと</div>
    <div class="name name__bottom">ささみ棒</div>
    <div class="name name__sub">（スライスタイプ）</div>
    <div class="tate tate--origin">（北海道産おやつ）</div>
    <div class="tate tate--claim-1">完全無添加</div>
    <div class="tate tate--claim-2">ヒューマングレード</div>
    <div class="scene" role="img" aria-label="跳ねる魚と小舟に乗った犬、和柄の波のイラスト"></div>
  </section>
  <section class="pouch pouch--d">
    <div class="pouch__hole"></div><div class="pouch__zip"></div>
    <div class="brand">ワン膳</div>
    <div class="label"></div>
    <div class="map" role="img" aria-label="北海道の地図イラスト"></div>
    <div class="name name__kanji">鶏</div>
    <div class="name name__top">カリッと</div>
    <div class="name name__bottom">ささみ棒</div>
    <div class="name name__sub">（スライスタイプ）</div>
    <div class="tate tate--origin">（北海道産おやつ）</div>
    <div class="tate tate--claim-1">完全無添加</div>
    <div class="tate tate--claim-2">ヒューマングレード</div>
    <div class="scene" role="img" aria-label="モノクロの魚と犬、波のイラスト"></div>
  </section>
</main>
</body>
</html>
```